KFL Noblesville Sign

I need to have a sign designed for a new self-storage facility we are going to be opening. The sign will be 4'W X 8'H.

Industry/Entity Type

Self Storage

Requirements
Must have
• Keystone Locker Hub logo at the top of the sign, under the logo I want the rendering.
• I also must have this information on the sign:
• 1. OPENING FALL 2016
• 2. Your premier self-storage facility.
• 3. www.keystonelockerhub.com

```html
<!DOCTYPE html>
<html lang="en">
<head>
<meta charset="utf-8">
<title>Keystone Locker Hub – Opening Sign</title>
<link rel="stylesheet" href="https://fonts.googleapis.com/css2?family=Oswald:wght@700&family=Archivo+Black&display=swap">
<style>
  :root {
    --brand-red: #d1232a;
    --brand-yellow: #f6ea37;
    --brand-green: #6cbb3c;
    --white: #ffffff;
    --photo-sky: #8f958c;
    --photo-wall: #c9b9a0;
    --photo-grass: #6f8a3a;
    --photo-shadow: #4f6a2a;
  }
  html, body {
    margin: 0;
    padding: 0;
    width: 1200px;
    height: 2400px;
    overflow: hidden;
    background: var(--brand-yellow);
  }
  .sign {
    display: block;
    width: 1200px;
    height: 2400px;
  }
  .band-red { fill: var(--brand-red); }
  .band-yellow { fill: var(--brand-yellow); }
  .panel-green { fill: var(--brand-green); }
  .brand-square { fill: var(--brand-yellow); }
  .brand-name {
    font-family: "Oswald", "Arial Narrow", sans-serif;
    font-weight: 700;
    fill: var(--white);
  }
  .headline {
    font-family: "Oswald", "Arial Narrow", sans-serif;
    font-weight: 700;
    fill: var(--brand-yellow);
  }
  .tagline {
    font-family: "Archivo Black", "Arial Black", sans-serif;
    fill: var(--white);
  }
  .web-address {
    font-family: "Oswald", "Arial Narrow", sans-serif;
    font-weight: 700;
    fill: var(--brand-red);
  }
</style>
</head>
<body>
<svg class="sign" viewBox="0 0 1200 2400" xmlns="http://www.w3.org/2000/svg">
  <defs>
    <linearGradient id="rendering-tones" x1="0" y1="0" x2="0" y2="1">
      <stop offset="0" stop-color="var(--photo-sky)"/>
      <stop offset="0.35" stop-color="var(--photo-wall)"/>
      <stop offset="0.62" stop-color="var(--photo-wall)"/>
      <stop offset="0.78" stop-color="var(--photo-grass)"/>
      <stop offset="1" stop-color="var(--photo-shadow)"/>
    </linearGradient>
  </defs>

  <!-- background bands -->
  <rect class="band-yellow" x="0" y="0" width="1200" height="2400"/>
  <polygon class="band-red" points="0,0 1200,0 1200,470 0,670"/>

  <!-- brand name -->
  <rect class="brand-square" x="80" y="110" width="90" height="90"/>
  <text class="brand-name" x="200" y="205" font-size="130">Keystone</text>
  <text class="brand-name" x="200" y="365" font-size="130">Locker Hub</text>

  <!-- facility rendering area -->
  <polygon points="0,710 1200,510 1200,1220 0,1340" fill="url(#rendering-tones)"
           role="img" aria-label="Architectural rendering of the new three-storey self-storage building with green roll-up doors on a lawn"/>

  <!-- opening panel -->
  <polygon class="panel-green" points="0,1330 980,1196 980,1760 0,1900"/>
  <text class="headline" x="110" y="1545" font-size="250" textLength="820" lengthAdjust="spacingAndGlyphs" transform="rotate(-7.8 110 1545)">OPENING</text>
  <text class="headline" x="110" y="1755" font-size="220" textLength="760" lengthAdjust="spacingAndGlyphs" transform="rotate(-7.8 110 1755)">FALL 2016</text>

  <!-- tagline panel -->
  <polygon class="band-red" points="0,1862 1080,1676 1080,2100 0,2230"/>
  <text class="tagline" x="60" y="1975" font-size="98" transform="rotate(-7.8 60 1975)">YOUR PREMIER</text>
  <text class="tagline" x="60" y="2080" font-size="98" transform="rotate(-7.8 60 2080)">SELF-STORAGE</text>
  <text class="tagline" x="60" y="2185" font-size="98" transform="rotate(-7.8 60 2185)">FACILITY.</text>

  <!-- web address -->
  <text class="web-address" x="1150" y="2330" font-size="66" text-anchor="end">www.keystonelockerhub.com</text>
</svg>
</body>
</html>
```